Poster Design Project - Front Window Poster for IT Business

Design a poster to be displayed in the front window of our office.
To include the following text:
Brightlane Systems Group
Servers & Networks
Deskora 720
Cloud Solutions
Helpdesk Services & Support
Network Audits
Disaster Recovery
IT Consulting
Contact details to be shown on the poster:
www.tk.com.au
02 5183 6214
Please also include the logo and related colour scheme.
Needs to look professional and easy to read from the street.
Must be in A1 format, printable through prontoleaf.

```html
<!DOCTYPE html>
<html lang="en">
<head>
<meta charset="utf-8">
<title>We Offer – TK Technology Solutions</title>
<link href="https://fonts.googleapis.com/css2?family=Fredoka:wght@700&family=Arimo:wght@400;700&family=Tinos&display=swap" rel="stylesheet">
<style>
  :root {
    --cyan: #0cf3ff;
    --cyan-soft: #7ff6f2;
    --royal: #1c3fcf;
    --navy-text: #1f3f99;
    --ink: #111111;
    --paper: #ffffff;
    --wash: #eef4fb;
  }
  html, body {
    margin: 0;
    padding: 0;
    overflow: hidden;
    background: var(--paper);
  }
  .poster {
    position: relative;
    width: 854px;
    height: 1200px;
    overflow: hidden;
    background: linear-gradient(160deg, var(--paper) 0%, var(--wash) 45%, var(--paper) 100%);
    font-family: "Arimo", Arial, sans-serif;
  }
  .headline {
    position: absolute;
    left: 0;
    top: 0;
    width: 854px;
    height: 215px;
    margin: 0;
  }
  .headline svg {
    display: block;
    width: 854px;
    height: 215px;
  }
  .headline-text {
    font-family: "Fredoka", "Arial Black", sans-serif;
    font-weight: 700;
    font-size: 184px;
  }
  .headline-shadow { fill: var(--royal); }
  .headline-face { fill: var(--cyan); }
  .headline-rule { fill: var(--cyan-soft); }
  .services {
    position: absolute;
    left: 132px;
    top: 314px;
    margin: 0;
    padding: 0;
    list-style: none;
  }
  .services li {
    position: relative;
    height: 89.3px;
    padding-left: 35px;
    font-size: 43px;
    line-height: 58px;
    white-space: nowrap;
    color: var(--ink);
  }
  .services li::before {
    content: "";
    position: absolute;
    left: 0;
    top: 21px;
    width: 17px;
    height: 17px;
    background: var(--cyan);
  }
  .contact {
    position: absolute;
    left: 127px;
    top: 1056px;
    margin: 0;
    padding: 0;
    list-style: none;
    font-family: "Tinos", "Times New Roman", serif;
    font-size: 28px;
    color: var(--navy-text);
  }
  .contact li {
    display: flex;
    align-items: center;
    height: 58px;
  }
  .contact svg {
    width: 28px;
    height: 28px;
    margin-right: 13px;
    fill: var(--cyan);
  }
  .brand {
    position: absolute;
    left: 628px;
    top: 1070px;
    width: 195px;
    text-align: center;
    font-family: "Arimo", Arial, sans-serif;
    font-weight: 700;
    color: var(--royal);
  }
  .brand-name {
    display: block;
    font-size: 70px;
    line-height: 72px;
    letter-spacing: 2px;
  }
  .brand-tagline {
    display: block;
    font-size: 13px;
    letter-spacing: 0.5px;
  }
</style>
</head>
<body>
<main class="poster">
  <h1 class="headline">
    <svg viewBox="0 0 854 215" aria-label="WE OFFER">
      <rect class="headline-rule" x="60" y="194" width="102" height="8"/>
      <rect class="headline-rule" x="240" y="194" width="560" height="8"/>
      <text class="headline-text headline-shadow" x="40" y="194" textLength="780" lengthAdjust="spacingAndGlyphs">WE OFFER</text>
      <text class="headline-text headline-face" x="33" y="187" textLength="780" lengthAdjust="spacingAndGlyphs">WE OFFER</text>
    </svg>
  </h1>

  <ul class="services">
    <li>Brightlane Systems Group</li>
    <li>Servers &amp; Networks</li>
    <li>Deskora 720</li>
    <li>Cloud Solutions</li>
    <li>Helpdesk Services &amp; Support</li>
    <li>Network Audits</li>
    <li>Disaster Recovery</li>
    <li>IT Consulting</li>
  </ul>

  <ul class="contact">
    <li>
      <svg viewBox="0 0 24 24" aria-hidden="true"><path d="M12 2 1 12h3v10h6v-6h4v6h6V12h3z"/></svg>
      www.tk.com.au
    </li>
    <li>
      <svg viewBox="0 0 24 24" aria-hidden="true"><path d="M2 4h20v4H2z"/><path d="M3 9h18v13H3z M6 12v2h3v-2z M10.5 12v2h3v-2z M15 12v2h3v-2z M6 16v2h3v-2z M10.5 16v2h3v-2z M15 16v2h3v-2z" fill-rule="evenodd"/></svg>
      02 5183 6214
    </li>
  </ul>

  <div class="brand">
    <span class="brand-name">TK</span>
    <span class="brand-tagline">TECHNOLOGY SOLUTIONS</span>
  </div>
</main>
</body>
</html>
```